Design My Bussiness Card
Technology company
Project: Design My Bussiness Card
Design My Bussiness Card -
Creative Brief
Professional
Dorian Pelkey
2847 E. Tollbrook #3
marisa@vantrelo.net
www.qoribelix.info

```html
<!DOCTYPE html>
<html lang="en">
<head>
<meta charset="utf-8">
<title>Qoribelix Stationery</title>
<link rel="stylesheet" href="https://fonts.googleapis.com/css2?family=Crimson+Text:wght@400;600&display=swap">
<style>
  :root {
    --paper: #ffffff;
    --canvas: #ffffff;
    --brand-green: #1f9a4b;
    --brand-brown: #3b2a1f;
    --ink: #3a3a3a;
    --edge: #d9d9d9;
    --font-text: "Crimson Text", "Times New Roman", serif;
  }
  html, body {
    margin: 0;
    padding: 0;
    width: 1200px;
    height: 1101px;
    overflow: hidden;
    background: var(--canvas);
    font-family: var(--font-text);
  }
  .stage {
    position: relative;
    width: 1200px;
    height: 1101px;
  }
  .piece {
    position: absolute;
    background: var(--paper);
    box-shadow: 0 0 0 1px var(--edge);
    overflow: hidden;
  }
  .piece > svg.shapes {
    position: absolute;
    inset: 0;
    width: 100%;
    height: 100%;
  }
  .green { fill: var(--brand-green); }
  .brown { fill: var(--brand-brown); }

  .brand {
    position: absolute;
    display: flex;
    align-items: center;
    gap: 8px;
    color: var(--brand-green);
  }
  .brand-dot {
    width: 30px;
    height: 30px;
    border-radius: 50%;
    background: var(--brand-green);
    flex: none;
  }
  .brand-text { display: flex; flex-direction: column; line-height: 1; }
  .brand-name {
    font-weight: 600;
    font-size: 34px;
    letter-spacing: 0.5px;
  }
  .brand-tagline {
    font-weight: 600;
    font-size: 10px;
    letter-spacing: 1px;
    text-transform: uppercase;
    margin-top: 3px;
  }

  /* Letterhead */
  .letterhead { left: 45px; top: 36px; width: 720px; height: 999px; }
  .letterhead .brand { left: 30px; top: 30px; }
  .letterhead-footer {
    position: absolute;
    left: 485px;
    top: 940px;
    font-size: 11px;
    line-height: 15px;
    color: var(--ink);
  }
  .letterhead-footer .web { color: var(--brand-green); font-weight: 600; }

  /* Business cards */
  .card-front { left: 855px; top: 36px; width: 315px; height: 159px; }
  .card-front .brand { left: 14px; top: 16px; gap: 5px; }
  .card-front .brand-dot { width: 16px; height: 16px; }
  .card-front .brand-name { font-size: 19px; }
  .card-front .brand-tagline { font-size: 5.5px; letter-spacing: 0.6px; margin-top: 2px; }
  .card-contact {
    position: absolute;
    left: 166px;
    top: 72px;
    color: var(--ink);
    font-size: 6.5px;
    line-height: 8.5px;
  }
  .card-contact .person {
    font-size: 12px;
    font-weight: 600;
    line-height: 16px;
    margin-bottom: 3px;
  }
  .card-back {
    left: 855px; top: 216px; width: 315px; height: 153px;
    background: var(--brand-brown);
    display: flex; align-items: center; justify-content: center;
  }
  .back-mark {
    color: var(--paper);
    font-weight: 600;
    font-size: 22px;
    letter-spacing: 1px;
  }

  /* Envelope */
  .envelope-body { left: 366px; top: 585px; width: 819px; height: 465px; }
  .envelope-body .brand { left: 30px; top: 60px; }
  .envelope-body .brand-name { font-size: 40px; }
  .envelope-body .brand-dot { width: 36px; height: 36px; }
  .envelope-return {
    position: absolute;
    right: 40px;
    bottom: 24px;
    font-size: 11px;
    color: var(--ink);
  }
  .envelope-flap {
    position: absolute;
    left: 366px;
    top: 420px;
    width: 819px;
    height: 200px;
  }
  .flap-mark {
    position: absolute;
    left: 366px;
    top: 468px;
    width: 819px;
    text-align: center;
    color: var(--paper);
    font-weight: 600;
    font-size: 20px;
    letter-spacing: 1px;
  }
</style>
</head>
<body>
<main class="stage">

  <section class="piece letterhead" aria-label="Letterhead">
    <svg class="shapes" viewBox="0 0 720 999" preserveAspectRatio="none" aria-hidden="true">
      <path class="green" d="M450 0 H720 V330 C690 150 600 40 450 0 Z"/>
      <path class="brown" d="M0 570 C60 790 200 940 400 999 H0 Z"/>
    </svg>
    <div class="brand">
      <span class="brand-dot"></span>
      <span class="brand-text">
        <span class="brand-name">Qoribelix</span>
        <span class="brand-tagline">Professional Business Services</span>
      </span>
    </div>
    <address class="letterhead-footer" style="font-style:normal">
      2847 E. Tollbrook #3 &nbsp;P: 773.555.0142<br>
      C: 773.555.0187 &nbsp;E: marisa@vantrelo.net<br>
      <span class="web">www.qoribelix.info</span>
    </address>
  </section>

  <section class="piece card-front" aria-label="Business card front">
    <svg class="shapes" viewBox="0 0 315 159" preserveAspectRatio="none" aria-hidden="true">
      <path class="green" d="M190 0 H315 V112 C302 55 255 12 190 0 Z"/>
      <path class="brown" d="M0 62 C18 115 65 148 128 159 H0 Z"/>
    </svg>
    <div class="brand">
      <span class="brand-dot"></span>
      <span class="brand-text">
        <span class="brand-name">Qoribelix</span>
        <span class="brand-tagline">Professional Business Services</span>
      </span>
    </div>
    <address class="card-contact" style="font-style:normal">
      <div class="person">Dorian Pelkey</div>
      2847 E. Tollbrook #3<br>
      P: 773.555.0142 &nbsp;C: 773.555.0187<br>
      marisa@vantrelo.net<br>
      www.qoribelix.info
    </address>
  </section>

  <section class="piece card-back" aria-label="Business card back">
    <span class="back-mark">Qoribelix</span>
  </section>

  <section class="piece envelope-body" aria-label="Envelope">
    <svg class="shapes" viewBox="0 0 819 465" preserveAspectRatio="none" aria-hidden="true">
      <path class="green" d="M560 0 H819 V205 C785 90 690 22 560 0 Z"/>
      <path class="brown" d="M0 150 C60 320 200 425 390 465 H0 Z"/>
    </svg>
    <div class="brand">
      <span class="brand-dot"></span>
      <span class="brand-text">
        <span class="brand-name">Qoribelix</span>
        <span class="brand-tagline">Professional Business Services</span>
      </span>
    </div>
    <div class="envelope-return">2847 E. Tollbrook #3</div>
  </section>

  <svg class="envelope-flap" viewBox="0 0 819 200" preserveAspectRatio="none" aria-hidden="true">
    <path class="brown" d="M0 165 L378 10 Q409 -3 440 10 L819 165 L819 178 Q409 150 0 178 Z"/>
  </svg>
  <div class="flap-mark">Qoribelix</div>

</main>
</body>
</html>
```